Powerpoint Presentation Template

Kindly design a business class Powepoint Presentation template for our business use. Please stick to our company colours or even pictures as shown on our website and Logo

```html
<!DOCTYPE html>
<html lang="en">
<head>
<meta charset="utf-8">
<title>Kestrel Properties – Presentation Template Slides</title>
<link rel="stylesheet" href="https://fonts.googleapis.com/css2?family=Titillium+Web:wght@600;700&family=Montserrat:wght@400;600;700&display=swap">
<style>
  :root{
    --board:#323c4e;
    --brand-red:#8b2c22;
    --charcoal:#3a3d44;
    --teal:#3d8a7a;
    --slide-bg:#f6f6f6;
    --panel-grey:#e8e8e8;
    --ring-grey:#dedede;
    --ink:#555a60;
    --white:#ffffff;
  }
  *{box-sizing:border-box;margin:0;padding:0}
  html,body{width:1200px;height:1200px;overflow:hidden;background:var(--board)}
  .board{position:relative;width:1200px;height:1200px;font-family:'Montserrat',sans-serif}
  .board-brand{position:absolute;left:196px;top:18px;color:var(--brand-red);font-family:'Montserrat',sans-serif;font-weight:700;line-height:1}
  .board-brand .name{display:block;font-size:38px;letter-spacing:1px}
  .board-brand .sub{display:block;font-size:24px;margin-top:4px;padding-left:28px}
  .board-note{position:absolute;left:646px;top:40px;color:var(--white);font-family:'Titillium Web',sans-serif;font-weight:600;font-size:17px;line-height:20px}
  .slide{position:absolute;width:320px;height:180px;box-shadow:0 3px 8px rgba(0,0,0,.35)}
  .slide svg{display:block;width:320px;height:180px}
  .s1{left:70px;top:295px}.s2{left:445px;top:295px}.s3{left:819px;top:295px}
  .s4{left:70px;top:501px}.s5{left:445px;top:501px}.s6{left:819px;top:501px}
  .s7{left:70px;top:712px}.s8{left:445px;top:712px}
  text{font-family:'Montserrat',sans-serif}
  .title{font-size:11px;font-weight:700;fill:var(--brand-red);letter-spacing:.5px}
  .logo-name{font-size:11px;font-weight:700;fill:var(--brand-red)}
  .body{font-size:3.6px;fill:var(--ink)}
  .head{font-size:4px;font-weight:700;fill:var(--charcoal)}
  .foot{font-size:4px;fill:var(--white)}
  .axis{font-size:4px;fill:var(--ink)}
  .tab-num{font-size:9px;font-weight:700;fill:var(--white)}
</style>
</head>
<body>
<main class="board">
  <div class="board-brand"><span class="name">KESTREL</span><span class="sub">Properties</span></div>
  <div class="board-note">Individual Slides - 01d<br>( Submission With Bigger Size - More Clarity)</div>

  <svg width="0" height="0" style="position:absolute">
    <defs>
      <g id="slide-frame">
        <rect width="400" height="225" fill="var(--slide-bg)"/>
        <text class="title" x="14" y="20">YOUR SLIDE TITLE HERE</text>
        <rect x="14" y="25" width="22" height="1.5" fill="var(--brand-red)"/>
        <text class="logo-name" x="386" y="19" text-anchor="end">KESTREL</text>
        <text class="logo-name" x="386" y="31" text-anchor="end" style="font-size:9px">Properties</text>
        <rect y="213" width="400" height="12" fill="var(--brand-red)"/>
        <polygon points="372,213 400,213 400,225 368,225" fill="#1e1e22"/>
        <text class="foot" x="11" y="220.5">Copyright © 2018 KESTREL PROPERTIES All rights reserved.</text>
        <text class="foot" x="362" y="220.5" text-anchor="end">www.kestrelprops.co.za</text>
      </g>
    </defs>
  </svg>

  <!-- Slide 57: line chart -->
  <section class="slide s1">
    <svg viewBox="0 0 400 225">
      <use href="#slide-frame"/>
      <text class="foot" x="386" y="220.5" text-anchor="end">57</text>
      <text class="body" x="14" y="50">Lorem Ipsum is simply dummy text of the printing and typesetting industry. Lorem Ipsum has been the industry's standard dummy text ever since</text>
      <text class="body" x="14" y="58">the 1500s, when an unknown printer took a galley of type and scrambled it</text>
      <rect x="16" y="74" width="222" height="120" fill="var(--panel-grey)"/>
      <polyline fill="none" stroke="var(--brand-red)" stroke-width="1.4"
        points="32,128 50,155 67,144 85,169 102,170 120,120 137,112 155,98 172,116 190,144 207,134 224,104"/>
      <g class="axis">
        <text x="34" y="125">65</text><text x="52" y="161">26</text><text x="69" y="142">45</text>
        <text x="87" y="171">12</text><text x="104" y="173">10</text><text x="122" y="118">75</text>
        <text x="139" y="110">83</text><text x="157" y="96">99</text><text x="174" y="115">78</text>
        <text x="192" y="144">45</text><text x="209" y="132">58</text><text x="226" y="102">91</text>
      </g>
      <g class="axis" text-anchor="middle">
        <text x="32" y="188">Jan</text><text x="50" y="188">Feb</text><text x="67" y="188">Mar</text>
        <text x="85" y="188">Apr</text><text x="102" y="188">May</text><text x="120" y="188">Jun</text>
        <text x="137" y="188">Jul</text><text x="155" y="188">Aug</text><text x="172" y="188">Sep</text>
        <text x="190" y="188">Oct</text><text x="207" y="188">Nov</text><text x="224" y="188">Dec</text>
      </g>
      <g class="body">
        <text x="262" y="86">Lorem Ipsum is simply dummy text of the</text>
        <text x="262" y="94">printing and typesetting industry.</text>
        <text x="262" y="112">Lorem Ipsum has been the industry's standard</text>
        <text x="262" y="120">dummy text ever since the 1500s.</text>
        <text x="262" y="138">When an unknown printer took a galley of type</text>
        <text x="262" y="146">and scrambled it to make a type specimen book.</text>
        <text x="262" y="164">It has survived not only five centuries, but also</text>
        <text x="262" y="172">the leap into electronic typesetting, remaining</text>
        <text x="262" y="180">unchanged.</text>
      </g>
    </svg>
  </section>

  <!-- Slide 58: ring with six points -->
  <section class="slide s2">
    <svg viewBox="0 0 400 225">
      <use href="#slide-frame"/>
      <text class="foot" x="386" y="220.5" text-anchor="end">58</text>
      <text class="body" x="14" y="50">Lorem Ipsum is simply dummy text of the printing and typesetting industry. Lorem Ipsum has been the industry's standard dummy text ever since</text>
      <text class="body" x="14" y="58">the 1500s, when an unknown printer took a galley of type and scrambled it</text>
      <circle cx="200" cy="135" r="51" fill="var(--brand-red)"/>
      <circle cx="200" cy="135" r="39" fill="var(--white)" stroke="#d9d9d9" stroke-width="2"/>
      <text class="logo-name" x="200" y="134" text-anchor="middle">KESTREL</text>
      <text class="logo-name" x="200" y="146" text-anchor="middle" style="font-size:9px">Properties</text>
      <g stroke="#aaa" stroke-width=".5" stroke-dasharray="1.5 1">
        <line x1="124" y1="93" x2="152" y2="93"/><line x1="114" y1="135" x2="130" y2="135"/><line x1="124" y1="177" x2="152" y2="177"/>
        <line x1="250" y1="93" x2="276" y2="93"/><line x1="270" y1="135" x2="286" y2="135"/><line x1="250" y1="177" x2="276" y2="177"/>
      </g>
      <g text-anchor="end">
        <text class="head" x="106" y="88">Title Goes Here</text>
        <text class="body" x="106" y="96">You simply add your own text and</text><text class="body" x="106" y="102">description here and is fully editable.</text>
        <text class="head" x="90" y="128">Title Goes Here</text>
        <text class="body" x="90" y="136">You simply add your own text and</text><text class="body" x="90" y="142">description here and is fully editable.</text>
        <text class="head" x="106" y="169">Title Goes Here</text>
        <text class="body" x="106" y="177">You simply add your own text and</text><text class="body" x="106" y="183">description here and is fully editable.</text>
      </g>
      <text class="head" x="288" y="88">Title Goes Here</text>
      <text class="body" x="288" y="96">You simply add your own text and</text><text class="body" x="288" y="102">description here and is fully editable.</text>
      <text class="head" x="308" y="128">Title Goes Here</text>
      <text class="body" x="308" y="136">You simply add your own text and</text><text class="body" x="308" y="142">description here and is fully editable.</text>
      <text class="head" x="288" y="169">Title Goes Here</text>
      <text class="body" x="288" y="177">You simply add your own text and</text><text class="body" x="288" y="183">description here and is fully editable.</text>
    </svg>
  </section>

  <!-- Slide 59: staircase steps -->
  <section class="slide s3">
    <svg viewBox="0 0 400 225">
      <use href="#slide-frame"/>
      <text class="foot" x="386" y="220.5" text-anchor="end">59</text>
      <polygon points="14,48 112,48 14,192" fill="var(--brand-red)"/>
      <polygon points="390,48 390,192 292,192" fill="var(--brand-red)"/>
      <g>
        <rect x="150" y="44" width="50" height="24" rx="2" fill="var(--brand-red)"/><text class="tab-num" x="180" y="60">05</text>
        <rect x="125" y="75" width="50" height="24" rx="2" fill="var(--charcoal)"/><text class="tab-num" x="155" y="91">04</text>
        <rect x="100" y="106" width="50" height="24" rx="2" fill="var(--brand-red)"/><text class="tab-num" x="130" y="122">03</text>
        <rect x="76" y="137" width="50" height="24" rx="2" fill="var(--charcoal)"/><text class="tab-num" x="106" y="153">02</text>
        <rect x="52" y="168" width="50" height="24" rx="2" fill="var(--brand-red)"/><text class="tab-num" x="82" y="184">01</text>
        <g fill="none" stroke="var(--white)" stroke-width="1.2">
          <rect x="156" y="50" width="14" height="12" rx="1"/><circle cx="138" cy="87" r="6"/>
          <ellipse cx="113" cy="114" rx="6" ry="2.5"/><path d="M107 114v8c0 1.5 12 1.5 12 0v-8"/>
          <path d="M83 144l6 3v8l-6-3zM89 147l6-3v8l-6 3"/><rect x="58" y="174" width="14" height="12" rx="1"/>
        </g>
      </g>
      <text class="head" x="210" y="54">Title Goes Here</text><text class="body" x="210" y="62">You simply add your own text and description here and is fully editable.</text>
      <text class="head" x="186" y="85">Title Goes Here</text><text class="body" x="186" y="93">You simply add your own text and description here and is fully editable.</text>
      <text class="head" x="162" y="116">Title Goes Here</text><text class="body" x="162" y="124">You simply add your own text and description here and is fully editable.</text>
      <text class="head" x="138" y="147">Title Goes Here</text><text class="body" x="138" y="155">You simply add your own text and description here and is fully editable.</text>
      <text class="head" x="114" y="181">Title Goes Here</text><text class="body" x="114" y="189">You simply add your own text and description here and is fully editable.</text>
    </svg>
  </section>

  <!-- Slide 60: honeycomb -->
  <section class="slide s4">
    <svg viewBox="0 0 400 225">
      <use href="#slide-frame"/>
      <text class="foot" x="386" y="220.5" text-anchor="end">60</text>
      <defs><polygon id="hex" points="0,-25 21.6,-12.5 21.6,12.5 0,25 -21.6,12.5 -21.6,-12.5"/></defs>
      <use href="#hex" x="174" y="78" fill="var(--charcoal)"/>
      <use href="#hex" x="220" y="78" fill="var(--brand-red)"/>
      <use href="#hex" x="151" y="118" fill="var(--brand-red)"/>
      <use href="#hex" x="197" y="118" fill="var(--white)" stroke="#ddd"/>
      <use href="#hex" x="243" y="118" fill="var(--charcoal)"/>
      <use href="#hex" x="174" y="158" fill="var(--charcoal)"/>
      <use href="#hex" x="220" y="158" fill="var(--brand-red)"/>
      <text class="logo-name" x="197" y="118" text-anchor="middle" style="font-size:7px">KESTREL</text>
      <text class="logo-name" x="197" y="126" text-anchor="middle" style="font-size:5px">Properties</text>
      <g fill="none" stroke="var(--white)" stroke-width="1">
        <rect x="169" y="71" width="10" height="13"/><circle cx="220" cy="78" r="6"/><circle cx="220" cy="78" r="2.5"/>
        <circle cx="151" cy="118" r="6"/><circle cx="243" cy="118" r="6"/>
        <ellipse cx="174" cy="154" rx="5" ry="2"/><path d="M169 154v8c0 1.5 10 1.5 10 0v-8"/>
        <path d="M215 164v-4M219 164v-7M223 164v-10"/>
      </g>
      <g text-anchor="end">
        <text class="head" x="124" y="72">Title Goes Here</text>
        <text class="body" x="124" y="80">You simply add your own text and</text><text class="body" x="124" y="86">description here and is fully editable.</text>
        <text class="head" x="108" y="112">Title Goes Here</text>
        <text class="body" x="108" y="120">You simply add your own text and</text><text class="body" x="108" y="126">description here and is fully editable.</text>
        <text class="head" x="124" y="152">Title Goes Here</text>
        <text class="body" x="124" y="160">You simply add your own text and</text><text class="body" x="124" y="166">description here and is fully editable.</text>
      </g>
      <text class="head" x="268" y="72">Title Goes Here</text>
      <text class="body" x="268" y="80">You simply add your own text and</text><text class="body" x="268" y="86">description here and is fully editable.</text>
      <text class="head" x="288" y="112">Title Goes Here</text>
      <text class="body" x="288" y="120">You simply add your own text and</text><text class="body" x="288" y="126">description here and is fully editable.</text>
      <text class="head" x="268" y="152">Title Goes Here</text>
      <text class="body" x="268" y="160">You simply add your own text and</text><text class="body" x="268" y="166">description here and is fully editable.</text>
    </svg>
  </section>

  <!-- Slide 61: wave timeline -->
  <section class="slide s5">
    <svg viewBox="0 0 400 225">
      <use href="#slide-frame"/>
      <text class="foot" x="386" y="220.5" text-anchor="end">61</text>
      <g fill="none" stroke-width="11">
        <circle cx="62" cy="118" r="25" stroke="var(--ring-grey)"/>
        <circle cx="116" cy="118" r="25" stroke="var(--ring-grey)"/>
        <circle cx="170" cy="118" r="25" stroke="var(--ring-grey)"/>
        <circle cx="224" cy="118" r="25" stroke="var(--ring-grey)"/>
        <circle cx="278" cy="118" r="25" stroke="var(--ring-grey)"/>
        <circle cx="332" cy="118" r="25" stroke="var(--ring-grey)"/>
        <path d="M37 118a25 25 0 0 1 50 0" stroke="var(--brand-red)"/>
        <path d="M91 118a25 25 0 0 0 50 0" stroke="var(--charcoal)"/>
        <path d="M145 118a25 25 0 0 1 50 0" stroke="var(--brand-red)"/>
        <path d="M199 118a25 25 0 0 0 50 0" stroke="var(--charcoal)"/>
        <path d="M253 118a25 25 0 0 1 50 0" stroke="var(--brand-red)"/>
        <path d="M307 118a25 25 0 0 0 50 0" stroke="var(--charcoal)"/>
      </g>
      <g fill="var(--charcoal)">
        <circle cx="59" cy="119" r="3"/><circle cx="66" cy="119" r="3"/>
        <circle cx="116" cy="116" r="4" fill="none" stroke="var(--charcoal)"/><rect x="114" y="121" width="4" height="3"/>
        <rect x="165" y="119" width="2" height="5"/><rect x="169" y="116" width="2" height="8"/><rect x="173" y="113" width="2" height="11"/>
        <polygon points="219,116 229,116 224,123"/>
        <circle cx="276" cy="120" r="4" fill="none" stroke="var(--charcoal)" stroke-width="2"/><circle cx="283" cy="113" r="2"/>
        <path d="M327 123l10-10-2 7z"/>
      </g>
      <g text-anchor="middle">
        <text class="head" x="116" y="64">Your Title Here</text><text class="body" x="116" y="72">You simply add your own text and</text><text class="body" x="116" y="78">description here and is fully editable.</text>
        <text class="head" x="224" y="64">Your Title Here</text><text class="body" x="224" y="72">You simply add your own text and</text><text class="body" x="224" y="78">description here and is fully editable.</text>
        <text class="head" x="332" y="64">Your Title Here</text><text class="body" x="332" y="72">You simply add your own text and</text><text class="body" x="332" y="78">description here and is fully editable.</text>
        <text class="head" x="62" y="172">Your Title Here</text><text class="body" x="62" y="180">You simply add your own text and</text><text class="body" x="62" y="186">description here and is fully editable.</text>
        <text class="head" x="170" y="172">Your Title Here</text><text class="body" x="170" y="180">You simply add your own text and</text><text class="body" x="170" y="186">description here and is fully editable.</text>
        <text class="head" x="278" y="172">Your Title Here</text><text class="body" x="278" y="180">You simply add your own text and</text><text class="body" x="278" y="186">description here and is fully editable.</text>
      </g>
    </svg>
  </section>

  <!-- Slide 62: pyramid chart -->
  <section class="slide s6">
    <svg viewBox="0 0 400 225">
      <use href="#slide-frame"/>
      <text class="foot" x="386" y="220.5" text-anchor="end">62</text>
      <text class="body" x="14" y="50">Lorem Ipsum is simply dummy text of the printing and typesetting industry. Lorem Ipsum has been the industry's standard dummy text ever since</text>
      <text class="body" x="14" y="58">the 1500s, when an unknown printer took a galley of type and scrambled it</text>
      <g stroke="#ccc" stroke-width=".5">
        <line x1="52" y1="168" x2="300" y2="168"/><line x1="52" y1="150" x2="300" y2="150"/>
        <line x1="52" y1="133" x2="300" y2="133"/><line x1="52" y1="116" x2="300" y2="116"/>
        <line x1="52" y1="168" x2="112" y2="80"/><line x1="300" y1="168" x2="340" y2="130"/>
        <line x1="112" y1="80" x2="340" y2="80"/>
      </g>
      <g class="axis"><text x="40" y="170">0</text><text x="40" y="153">2</text><text x="40" y="136">4</text><text x="40" y="119">6</text></g>
      <g>
        <polygon points="110,85 102,132 120,132" fill="var(--charcoal)"/>
        <polygon points="160,88 152,130 170,130" fill="var(--charcoal)"/>
        <polygon points="208,98 200,128 218,128" fill="var(--charcoal)"/>
        <polygon points="252,110 244,126 262,126" fill="var(--charcoal)"/>
        <polygon points="298,116 290,124 308,124" fill="var(--charcoal)"/>
        <polygon points="90,104 80,150 100,150" fill="var(--teal)"/>
        <polygon points="140,112 130,148 150,148" fill="var(--teal)"/>
        <polygon points="193,124 183,146 203,146" fill="var(--teal)"/>
        <polygon points="240,130 230,144 250,144" fill="var(--teal)"/>
        <polygon points="286,136 276,142 296,142" fill="var(--teal)"/>
        <polygon points="77,134 66,170 88,170" fill="var(--brand-red)"/>
        <polygon points="128,140 117,168 139,168" fill="var(--brand-red)"/>
        <polygon points="174,150 163,166 185,166" fill="var(--brand-red)"/>
        <polygon points="220,158 209,164 231,164" fill="var(--brand-red)"/>
        <polygon points="266,160 255,162 277,162" fill="var(--brand-red)"/>
      </g>
      <g class="axis">
        <text x="106" y="82">6</text><text x="156" y="85">5</text><text x="204" y="95">4</text><text x="248" y="107">3</text><text x="294" y="113">2</text>
        <text x="88" y="101">4</text><text x="138" y="109">4</text><text x="190" y="121">2</text><text x="237" y="127">2</text><text x="283" y="133">1</text>
        <text x="316" y="140">Sales 2</text><text x="308" y="150">Sales 1</text><text x="296" y="162">Revenue</text>
      </g>
      <g class="axis" text-anchor="middle">
        <text x="80" y="182">Title - 01</text><text x="127" y="182">Title - 02</text><text x="174" y="182">Title - 03</text>
        <text x="220" y="182">Title - 04</text><text x="266" y="182">Title - 05</text>
      </g>
    </svg>
  </section>

  <!-- Slide 63: laptop showcase -->
  <section class="slide s7">
    <svg viewBox="0 0 400 225">
      <use href="#slide-frame"/>
      <text class="foot" x="386" y="220.5" text-anchor="end">63</text>
      <defs>
        <linearGradient id="dusk" x1="0" y1="0" x2="0" y2="1">
          <stop offset="0" stop-color="#5c6e8a"/><stop offset=".6" stop-color="#3c2e2a"/><stop offset="1" stop-color="#7a5a40"/>
        </linearGradient>
      </defs>
      <rect x="32" y="64" width="144" height="92" rx="4" fill="#222"/>
      <rect x="37" y="69" width="134" height="82" fill="url(#dusk)" role="img" aria-label="Photo of a modern apartment building at dusk"/>
      <path d="M16 158h176l-6 6H22z" fill="#c9c9c9"/>
      <g class="body">
        <text x="206" y="72">Lorem Ipsum is simply dummy text of the printing and typesetting</text>
        <text x="206" y="80">industry. Lorem Ipsum has been the industry's standard dummy</text>
        <text x="206" y="88">text ever since the 1500s. When an unknown printer took a galley</text>
        <text x="206" y="96">of type and scrambled it to make a type specimen book.</text>
      </g>
      <circle cx="214" cy="131" r="7" fill="var(--brand-red)"/><path d="M210 131l3 3 5-6" fill="none" stroke="var(--white)" stroke-width="1.5"/>
      <circle cx="307" cy="131" r="7" fill="var(--brand-red)"/><path d="M303 131l3 3 5-6" fill="none" stroke="var(--white)" stroke-width="1.5"/>
      <text class="head" x="229" y="128">Title Goes Here</text>
      <text class="body" x="229" y="135">You simply add your own</text><text class="body" x="229" y="141">text and description here</text><text class="body" x="229" y="147">and is fully editable.</text>
      <text class="head" x="322" y="128">Title Goes Here</text>
      <text class="body" x="322" y="135">You simply add your own</text><text class="body" x="322" y="141">text and description here</text><text class="body" x="322" y="147">and is fully editable.</text>
      <text class="body" x="30" y="190">Lorem Ipsum is simply dummy text of the printing and typesetting industry. Lorem Ipsum has been the industry's standard dummy text</text>
      <text class="body" x="30" y="198">ever since the 1500s. When an unknown printer took a galley of type and scrambled it to make a type specimen book.</text>
    </svg>
  </section>

  <!-- Slide: thank you -->
  <section class="slide s8">
    <svg viewBox="0 0 400 225">
      <defs>
        <linearGradient id="aerial" x1="0" y1="0" x2="1" y2="1">
          <stop offset="0" stop-color="#6b6458"/><stop offset=".5" stop-color="#4d4e52"/><stop offset="1" stop-color="#6e6a62"/>
        </linearGradient>
      </defs>
      <rect width="400" height="225" fill="var(--slide-bg)"/>
      <rect width="400" height="142" fill="url(#aerial)" role="img" aria-label="Aerial photo of a residential apartment complex"/>
      <text x="370" y="42" text-anchor="end" style="font-size:15px;font-weight:700;fill:var(--white)">THANK YOU</text>
      <text class="logo-name" x="20" y="165" style="font-size:13px">KESTREL</text>
      <text class="logo-name" x="30" y="178" style="font-size:10px">Properties</text>
      <text class="head" x="28" y="190" style="font-size:3.6px">www.kestrelprops.co.za</text>
      <text class="head" x="28" y="197" style="font-size:3.6px">info@kestrelprops.com</text>
      <g class="body">
        <text class="head" x="163" y="164" style="font-size:3.6px">Head Office</text>
        <text x="163" y="172">42 Acacia Lane</text><text x="163" y="177">Parkview,</text><text x="163" y="182">Midrand, 1685</text>
        <text x="163" y="187">Tel: +27 10 555 0140</text><text x="163" y="192">Fax: +27 10 555 0141</text>
        <text class="head" x="233" y="164" style="font-size:3.6px">PRETORIA OFFICE</text>
        <text x="233" y="172">2nd Floor Bloom Centre</text><text x="233" y="177">88 Jacaranda Street</text><text x="233" y="182">Brooklyn, 0181</text>
        <text x="233" y="187">Tel: +27 12 555 0190</text><text x="233" y="192">Fax: +27 12 555 0191</text>
        <text class="head" x="311" y="164" style="font-size:3.6px">TZANEEN OFFICE</text>
        <text x="311" y="172">7 Marula Avenue</text><text x="311" y="177">Tzaneen, 0850</text>
        <text x="311" y="182">Tel: +27 15 555 0120</text><text x="311" y="187">Fax: +27 15 555 0121</text>
      </g>
    </svg>
  </section>
</main>
</body>
</html>
```